Company Capability Statement

We need company Capability Statement designed. 2 page.(A4) in logo colours.
Info in downloads word doc. Please see I have added in world doc- excavator in our services

```html
<!DOCTYPE html>
<html lang="en">
<head>
<meta charset="utf-8">
<title>Ridgeline Commercial – Capability Statement</title>
<link href="https://fonts.googleapis.com/css2?family=Montserrat:wght@500;600;700;800;900&family=Poppins:wght@400;500;600;700&display=swap" rel="stylesheet">
<style>
:root{
  --green-dark:#0d6428;
  --green:#167a34;
  --green-mid:#2f8f3c;
  --lime:#8dc63f;
  --lime-light:#b9dc7c;
  --ink:#1d1d1d;
  --grey:#555;
  --paper:#ffffff;
  --bg:#a4a7ae;
}
*{box-sizing:border-box;margin:0;padding:0}
html,body{width:1200px;height:3518px;overflow:hidden;background:var(--bg)}
body{position:relative;font-family:'Poppins',sans-serif;color:var(--ink)}
.page{position:absolute;left:10px;width:1180px;height:1669px;background:var(--paper);overflow:hidden;box-shadow:0 4px 18px rgba(0,0,0,.25)}
.page-one{top:60px}
.page-two{top:1789px}
.abs{position:absolute}
.deco{position:absolute;left:0;top:0}
.brand{display:flex;align-items:center;gap:14px;font-family:'Montserrat',sans-serif;font-weight:900;color:var(--green);letter-spacing:1px}
.brand-dot{width:54px;height:54px;border-radius:50%;background:var(--lime);flex:none}
.brand-name{font-size:40px;line-height:1}

/* page one */
.hero-title{left:47px;top:258px;font-family:'Montserrat',sans-serif;font-weight:900;color:#fff;font-size:48px;line-height:55px;text-transform:uppercase;white-space:nowrap}
.hero-title small{font-size:28px;font-weight:800}
.region-pill{left:47px;top:510px;width:537px;height:46px;border:2px solid var(--lime);color:var(--lime);font-family:'Montserrat',sans-serif;font-weight:700;font-size:22px;display:flex;align-items:center;justify-content:center}
.intro{left:47px;top:594px;width:640px;font-size:15px;line-height:19.5px;color:#333}
.intro p{margin-bottom:13px}
.intro b{color:var(--green);font-weight:600}
.intro-mark{left:47px;top:592px;width:28px;height:36px;background:var(--lime)}
.section-head{left:0;width:1180px;text-align:center;font-family:'Montserrat',sans-serif;font-weight:800;color:var(--green);font-size:34px;line-height:42px}
.section-head::before,.section-head::after{content:"";display:inline-block;vertical-align:middle;width:260px;height:10px;margin:0 14px;background:linear-gradient(90deg,var(--lime) 0 8%,transparent 8% 10%,var(--lime) 10% 18%,transparent 18% 20%,var(--lime) 20% 28%,transparent 28% 31%,var(--green) 31% 100%)}
.section-head::after{transform:scaleX(-1)}
.service{width:351px;height:180px;border:2px solid var(--green-mid);border-radius:6px;padding:0 12px;background:#fff}
.service h3{position:absolute;top:-17px;left:50%;transform:translateX(-50%);background:#fff;padding:0 10px;font-family:'Montserrat',sans-serif;font-weight:700;font-size:21px;line-height:30px;color:var(--ink);white-space:nowrap}
.service .label{margin:26px 0 12px;height:44px;background:linear-gradient(90deg,#fff,var(--lime-light) 50%,#fff);display:flex;align-items:center;justify-content:center;text-align:center;font-family:'Montserrat',sans-serif;font-weight:700;font-size:12.5px;line-height:16px;text-transform:uppercase}
.service ul{list-style:none;display:grid;grid-template-rows:repeat(3,auto);grid-auto-flow:column;grid-template-columns:42% 58%;font-size:14px;line-height:17px;row-gap:5px}
.service li{padding-left:18px;position:relative}
.service li::before{content:"";position:absolute;left:2px;top:3px;border-left:10px solid var(--green-mid);border-top:6px solid transparent;border-bottom:6px solid transparent}
.industries{left:47px;top:1270px;width:1087px;height:143px;background:var(--green)}
.industries-tab{left:299px;top:1247px;width:586px;height:52px;background:var(--lime);color:var(--green-dark);font-family:'Montserrat',sans-serif;font-weight:800;font-size:31px;display:flex;align-items:center;justify-content:center}
.industry-grid{position:absolute;left:26px;top:50px;right:20px;display:grid;grid-template-columns:232px 292px 262px 1fr;row-gap:16px;color:#fff;font-size:15px;font-weight:500}
.industry-grid span{display:flex;align-items:center;gap:10px}
.tick{width:20px;height:20px;border-radius:50%;border:2px solid var(--lime);flex:none;position:relative}
.tick::after{content:"";position:absolute;left:5px;top:2px;width:5px;height:9px;border:solid var(--lime);border-width:0 2px 2px 0;transform:rotate(45deg)}
.why-title{left:47px;top:1444px;font-family:'Montserrat',sans-serif;font-weight:800;color:var(--green);font-size:38px;line-height:43px}
.why-grid{left:230px;top:1446px;width:920px;display:grid;grid-template-columns:250px 232px 200px 1fr;row-gap:18px;font-size:15px;line-height:18px;color:#333}
.why-grid div{display:flex;align-items:center;gap:10px}
.icon{display:block;width:46px;height:46px;border-radius:50%;background:var(--green);border:3px solid #fff;box-shadow:0 0 0 2px var(--green);flex:none;position:relative}
.icon::after{content:"";position:absolute;left:12px;top:12px;width:16px;height:16px;border-radius:50%;border:3px solid #fff}
.footer{left:0;top:1596px;width:1180px;height:54px}
.footer-mail{left:0;top:0;width:780px;height:54px;background:var(--lime);color:var(--green-dark);font-size:19px;font-weight:500;display:flex;align-items:center;padding-left:47px}
.footer-phone{right:0;top:0;width:330px;height:54px;background:var(--green);color:#fff;font-family:'Montserrat',sans-serif;font-weight:800;font-size:32px;display:flex;align-items:center;justify-content:center;gap:12px}

/* page two */
.fleet{width:351px;height:327px;border:2px solid var(--green-mid);border-radius:6px;overflow:hidden;text-align:center;box-shadow:0 12px 12px -10px rgba(0,0,0,.35)}
.fleet header{background:var(--green);color:#fff;height:82px;display:flex;flex-direction:column;justify-content:center;font-family:'Montserrat',sans-serif;font-size:22px;line-height:26px}
.fleet header b{font-weight:700}
.fleet header span{font-weight:500}
.fleet ul{list-style:none;padding:8px 16px 0;font-size:14px;font-weight:700}
.fleet li{border-bottom:1px solid #d5d5d5;padding:7px 0}
.fleet li em{font-style:normal;color:var(--green-mid)}
.fleet .avail{display:inline-block;background:var(--lime);color:#fff;padding:2px 26px;border:none;margin-top:2px}
.fleet p{font-size:14px;line-height:17px;color:#555;padding:14px 18px 0}
.safety{left:47px;top:524px;width:1087px;height:298px;background:var(--green)}
.safety-tab{left:264px;top:500px;width:654px;height:92px;background:var(--lime);text-align:center;color:var(--green-dark);font-family:'Montserrat',sans-serif}
.safety-tab h2{font-size:34px;font-weight:800;line-height:44px;margin-top:10px}
.safety-tab p{font-size:15px;font-weight:700;line-height:20px}
.committed{left:47px;top:606px;width:1087px;text-align:center;color:#fff;font-family:'Montserrat',sans-serif;font-weight:600;font-size:13px;letter-spacing:1px}
.safety-grid{left:47px;top:640px;width:1087px;display:grid;grid-template-columns:repeat(5,1fr);color:#fff;font-size:14px;font-weight:600;text-align:center;line-height:17px}
.safety-grid div{border-right:1px solid rgba(255,255,255,.4);padding:10px 10px 0;height:164px}
.safety-grid div:last-child{border-right:none}
.safety-grid .icon{margin:0 auto 18px;width:58px;height:58px;background:transparent;box-shadow:0 0 0 3px #fff;border-color:var(--green)}
.safety-grid .icon::after{left:17px;top:17px}
.area{left:437px;top:868px;width:320px;text-align:center;font-size:14px;line-height:17px;color:#333}
.area h2,.commit h2{font-family:'Montserrat',sans-serif;font-weight:800;color:var(--green);font-size:26px;line-height:32px;margin-bottom:8px}
.area h3{color:var(--green);font-size:17px;line-height:22px;font-weight:700;margin-top:6px}
.area h3 + p{border-top:1px solid #aaa;margin:2px 20px 0;padding-top:2px}
.commit{left:820px;top:868px;width:314px;text-align:center}
.commit h2{border-bottom:1px solid #999;padding-bottom:6px}
.commit p{font-size:14px;font-weight:700;line-height:17px;color:#222;margin-top:10px}
.call-tab{left:600px;top:1145px;width:440px;height:62px;background:var(--lime);color:var(--green-dark);font-family:'Montserrat',sans-serif;font-weight:900;font-size:34px;display:flex;align-items:center;justify-content:center}
.call-phone{left:560px;top:1218px;width:520px;text-align:center;color:#fff;font-family:'Montserrat',sans-serif;font-weight:800;font-size:60px;line-height:74px}
.call-line{left:560px;width:520px;text-align:center;color:#fff;font-weight:600;font-size:25px;line-height:32px}
.slogan{left:405px;top:1488px;width:395px;text-align:right;font-family:'Montserrat',sans-serif;font-weight:800;color:var(--green);font-size:31px;line-height:40px;white-space:nowrap}
.slogan p{font-family:'Poppins',sans-serif;font-size:13px;font-weight:600;color:var(--ink);line-height:24px}
.sign-rule{left:828px;top:1485px;width:2px;height:140px;background:#bbb}
.brand-bottom{left:860px;top:1522px}
.brand-bottom .brand-name{font-size:30px}
.brand-bottom .brand-dot{width:44px;height:44px}
</style>
</head>
<body>

<section class="page page-one">
  <svg class="deco" width="1180" height="1669" viewBox="0 0 1180 1669">
    <defs>
      <linearGradient id="photoCrusher" x1="0" y1="0" x2="1" y2="1">
        <stop offset="0" stop-color="#5f6b4c"/><stop offset=".5" stop-color="#c79a2a"/><stop offset="1" stop-color="#8b7a60"/>
      </linearGradient>
      <linearGradient id="photoTruck" x1="0" y1="0" x2="1" y2="0">
        <stop offset="0" stop-color="#e8e8e8"/><stop offset=".4" stop-color="#b33a3a"/><stop offset=".7" stop-color="#c89a32"/><stop offset="1" stop-color="#6f7a5a"/>
      </linearGradient>
    </defs>
    <rect x="0" y="216" width="1180" height="382" fill="var(--green)"/>
    <circle cx="980" cy="400" r="345" fill="var(--green)"/>
    <path d="M626 337 A360 360 0 0 1 917 45" fill="none" stroke="var(--lime)" stroke-width="12"/>
    <path d="M917 755 A360 360 0 0 1 704 631" fill="none" stroke="var(--lime)" stroke-width="12"/>
    <circle cx="980" cy="400" r="300" fill="#fff"/>
    <circle cx="980" cy="400" r="292" fill="url(#photoCrusher)" role="img" aria-label="Photo of a tracked mobile screening plant on site"/>
    <rect x="124" y="1064" width="931" height="186" rx="4" fill="url(#photoTruck)" role="img" aria-label="Photo of a prime mover and low loader carrying an excavator and crushing plant"/>
  </svg>

  <div class="abs brand" style="left:49px;top:60px"><span class="brand-dot"></span><span class="brand-name">RIDGELINE<br>COMMERCIAL</span></div>

  <h1 class="abs hero-title"><small>Mobile</small> Crushing,<br>Screening<br><small>&amp;</small> Resource<br>Recovery <small>Solutions</small></h1>
  <div class="abs region-pill">South East Queensland &amp; Northern NSW</div>

  <div class="abs intro-mark"></div>
  <div class="abs intro">
    <p>&nbsp;&nbsp;&nbsp;&nbsp;&nbsp;&nbsp;&nbsp;<b>Ridgeline Commercial</b> provides mobile crushing, screening, and resource recovery services for civil construction, demolition, infrastructure, commercial, and development projects. Using modern mobile equipment, we process construction and demolition materials directly on-site, helping clients reduce waste, lower project costs, and maximise the reuse of valuable resources.</p>
    <p>Our flexible mobile service delivers efficient, cost-effective, and environmentally responsible solutions wherever your project is located.</p>
  </div>

  <h2 class="abs section-head" style="top:822px">OUR SERVICES</h2>

  <div class="abs service" style="left:47px;top:882px">
    <h3>Mobile Crushing</h3>
    <div class="label">Processing of</div>
    <ul><li>Concrete</li><li>Brick</li><li>Asphalt</li><li>Rock</li><li>Construction &amp; demolition waste</li></ul>
  </div>
  <div class="abs service" style="left:416px;top:882px">
    <h3>Mobile Screening</h3>
    <div class="label">Separation and classification of</div>
    <ul style="grid-template-columns:30% 70%"><li>Soil</li><li>Sand</li><li>Gravel</li><li>Recycled aggregates</li><li>Landscaping materials</li></ul>
  </div>
  <div class="abs service" style="left:783px;top:882px">
    <h3>Resource Recovery</h3>
    <div class="label">Transforming waste materials<br>into reusable products for</div>
    <ul style="grid-template-columns:38% 62%"><li>Road base</li><li>Sub-base</li><li>Structural fill</li><li>Hardstands</li><li>Drainage applications</li><li>Landscaping projects</li></ul>
  </div>

  <div class="abs industries">
    <div class="industry-grid">
      <span><i class="tick"></i>Civil Construction</span>
      <span><i class="tick"></i>Infrastructure Projects</span>
      <span><i class="tick"></i>Property Development</span>
      <span><i class="tick"></i>Earthmoving Contractors</span>
      <span><i class="tick"></i>Demolition</span>
      <span><i class="tick"></i>Commercial Construction</span>
      <span><i class="tick"></i>Local Government</span>
      <span><i class="tick"></i>Quarry &amp; Resource Projects</span>
    </div>
  </div>
  <div class="abs industries-tab">INDUSTRIES WE SERVE</div>

  <h2 class="abs why-title">WHY<br>CHOOSE<br>US?</h2>
  <div class="abs why-grid">
    <div><i class="icon"></i>Mobile on-site<br>processing</div>
    <div><i class="icon"></i>Reduced transport<br>and landfill costs</div>
    <div><i class="icon"></i>Modern, reliable<br>equipment</div>
    <div><i class="icon"></i>Safe and professional<br>operations</div>
    <div><i class="icon"></i>Excavator feeding<br>&amp; material handling<br>available</div>
    <div><i class="icon"></i>Sustainable<br>recycling solutions</div>
    <div><i class="icon"></i>Fast<br>mobilisation</div>
    <div><i class="icon"></i>Flexible service<br>across SEQ and<br>Northern NSW</div>
  </div>

  <div class="abs footer">
    <div class="abs footer-mail">info@ridgelinecommercial.com.au&nbsp;&nbsp;|&nbsp;&nbsp;www.ridgelinecommercial.com.au</div>
    <div class="abs footer-phone">
      <svg width="30" height="30" viewBox="0 0 24 24"><path fill="#fff" d="M6.6 10.8a15 15 0 0 0 6.6 6.6l2.2-2.2c.3-.3.7-.4 1-.2 1.1.4 2.3.6 3.6.6.6 0 1 .4 1 1V20c0 .6-.4 1-1 1A17 17 0 0 1 3 4c0-.6.4-1 1-1h3.5c.6 0 1 .4 1 1 0 1.3.2 2.5.6 3.6.1.3 0 .7-.2 1z"/></svg>
      0400 512 780
    </div>
  </div>
</section>

<section class="page page-two">
  <svg class="deco" width="1180" height="1669" viewBox="0 0 1180 1669">
    <defs>
      <linearGradient id="mapFill" x1="0" y1="0" x2="1" y2="0">
        <stop offset="0" stop-color="#e6ece4"/><stop offset=".7" stop-color="#d6e9f2"/><stop offset="1" stop-color="#ffffff"/>
      </linearGradient>
      <linearGradient id="photoExcavator" x1="0" y1="0" x2="1" y2="1">
        <stop offset="0" stop-color="#d08a22"/><stop offset=".6" stop-color="#7a6a45"/><stop offset="1" stop-color="#3f6a34"/>
      </linearGradient>
    </defs>
    <rect x="0" y="822" width="560" height="255" fill="url(#mapFill)" role="img" aria-label="Map of South East Queensland and Northern New South Wales coast"/>
    <rect x="0" y="1077" width="1180" height="357" fill="var(--green)"/>
    <circle cx="190" cy="1275" r="285" fill="var(--green)"/>
    <path d="M-97 1171 A305 305 0 0 1 342 1011" fill="none" stroke="var(--lime)" stroke-width="10"/>
    <path d="M454 1427 A305 305 0 0 1 137 1575" fill="none" stroke="var(--lime)" stroke-width="10"/>
    <circle cx="190" cy="1275" r="270" fill="#fff"/>
    <circle cx="190" cy="1275" r="262" fill="url(#photoExcavator)" role="img" aria-label="Photo of a compact excavator beside a mobile jaw crusher"/>
  </svg>

  <h2 class="abs section-head" style="top:48px">OUR FLEET</h2>

  <article class="abs fleet" style="left:47px;top:127px">
    <header><b>StoneBreaker SB-J65</b><span>Jaw Crusher</span></header>
    <ul>
      <li>Diesel-powered <em>engine</em></li>
      <li>Overband magnet <em>conveyor</em></li>
      <li>Remote-control <em>tracking</em></li>
      <li>Up to 50 tonnes per hour <em>production</em></li>
    </ul>
    <p>Designed for efficient crushing of concrete, brick, asphalt, and demolition materials directly on site.</p>
  </article>
  <article class="abs fleet" style="left:416px;top:127px">
    <header><b>StoneBreaker SB-S48</b><span>Screening Plant</span></header>
    <ul>
      <li>Diesel-powered <em>engine</em></li>
      <li>Two-deck, three-way <em>screen</em></li>
      <li>Remote-control <em>tracking</em></li>
      <li>Up to 70 tonnes per hour <em>production</em></li>
    </ul>
    <p>Provides efficient material separation and production of quality recycled aggregates.</p>
  </article>
  <article class="abs fleet" style="left:783px;top:127px">
    <header><b>Excavator &amp; Material</b><span>Handling Equipment</span></header>
    <ul>
      <li class="avail">Available to support</li>
      <li>Crusher <em>feeding</em></li>
      <li>Screening plant <em>feeding</em></li>
      <li>Stockpile <em>management</em></li>
      <li>Material <em>sorting and recovery</em></li>
    </ul>
    <p>Helping maintain continuous production and efficient site operations.</p>
  </article>

  <div class="abs safety"></div>
  <div class="abs safety-tab"><h2>SAFETY &amp; COMPLIANCE</h2><p>SAFETY IS AT THE CORE OF EVERYTHING WE DO</p></div>
  <div class="abs committed">— RIDGELINE COMMERCIAL IS COMMITTED TO —</div>
  <div class="abs safety-grid">
    <div><i class="icon"></i>Safe Work<br>Method Statements<br>(SWMS)</div>
    <div><i class="icon"></i>Site-specific<br>risk<br>assessments</div>
    <div><i class="icon"></i>Qualified<br>operators</div>
    <div><i class="icon"></i>Maintained<br>and compliant<br>equipment</div>
    <div><i class="icon"></i>Environmentally<br>responsible<br>work practices</div>
  </div>

  <div class="abs area">
    <h2>SERVICE AREA</h2>
    <h3>South East Queensland</h3>
    <p>Brisbane | Gold Coast | Sunshine Coast | Ipswich Logan | Scenic Rim</p>
    <h3>Northern New South Wales</h3>
    <p>Tweed Coast | Northern Rivers | Border Region</p>
  </div>
  <div class="abs commit">
    <h2>OUR COMMITMENT</h2>
    <p>Delivering reliable mobile crushing, screening, and resource recovery solutions that help clients reduce costs, minimise waste, and improve project outcomes.</p>
  </div>

  <div class="abs call-tab">CALL US TODAY!</div>
  <div class="abs call-phone">0400 512 780</div>
  <div class="abs call-line" style="top:1308px">✉ info@ridgelinecommercial.com.au</div>
  <div class="abs call-line" style="top:1350px">www.ridgelinecommercial.com.au</div>

  <div class="abs slogan">SMARTER RECYCLING.<br>BETTER OUTCOMES.<p>Mobile Crushing | Mobile Screening | Resource Recovery</p></div>
  <div class="abs sign-rule"></div>
  <div class="abs brand brand-bottom"><span class="brand-dot"></span><span class="brand-name">RIDGELINE<br>COMMERCIAL</span></div>
</section>

</body>
</html>
```